Business card for utility of the future

I need a business card template designed for brivolo. We provide sustainable water, energy and waste services to homes.

The card should include name, position, email address, phone number, website and our logo (attached). I would like it to convey professionalism and creativity.

Target Market(s)

Homeowners, investors, corporate partners.

Industry/Entity Type

Utility

Contact Information for Business Card

The card should include name, position, email address, phone number, website and our logo (attached).

```html
<!DOCTYPE html>
<html lang="en">
<head>
<meta charset="utf-8">
<title>brivolo – Business Card</title>
<link rel="stylesheet" href="https://fonts.googleapis.com/css2?family=Lato:wght@400;700&display=swap">
<style>
  :root {
    --page-bg: #d8d3cb;
    --card-bg: #f1f1ef;
    --card-bg-edge: #e4e4e1;
    --brand-green: #2e8b47;
    --brand-orange: #d2553a;
    --ink: #262626;
  }
  * { margin: 0; padding: 0; box-sizing: border-box; }
  html, body {
    width: 1200px; height: 970px; overflow: hidden;
    background: var(--page-bg);
    font-family: "Lato", Arial, sans-serif;
  }
  .card {
    position: absolute; left: 80px; top: 190px;
    width: 1040px; height: 590px;
    border-radius: 24px; overflow: hidden;
    background: linear-gradient(135deg, var(--card-bg) 0%, var(--card-bg-edge) 100%);
    box-shadow: 0 18px 40px rgba(0,0,0,0.18);
    color: var(--ink);
  }
  .accent-dot {
    position: absolute; left: -37px; top: 65px;
    width: 74px; height: 74px; border-radius: 50%;
    background: var(--brand-orange);
  }
  .holder { position: absolute; left: 55px; top: 64px; }
  .holder-name {
    font-weight: 700; font-size: 37px; line-height: 44px;
    color: var(--brand-green); letter-spacing: 0.2px;
  }
  .holder-role { font-size: 31px; line-height: 36px; font-weight: 400; }
  .brand {
    position: absolute; right: 60px; top: 70px;
    font-weight: 700; font-size: 104px; line-height: 120px;
    color: var(--ink);
  }
  .address {
    position: absolute; left: 55px; top: 322px;
    font-size: 31px; line-height: 40px;
  }
  .contacts { position: absolute; left: 55px; top: 434px; list-style: none; }
  .contacts li {
    display: flex; align-items: center; gap: 12px;
    font-size: 31px; line-height: 40px;
  }
  .contacts svg { width: 31px; height: 31px; flex: none; }
  .website {
    position: absolute; right: 55px; top: 474px;
    font-size: 30px; line-height: 40px; font-weight: 700;
  }
  .website .site-name { color: var(--brand-green); font-weight: 400; }
  .band { position: absolute; left: 0; bottom: 0; width: 100%; height: 26px; display: flex; }
  .band-green { flex: none; width: 49.7%; background: var(--brand-green); }
  .band-orange { flex: 1; background: var(--brand-orange); }
</style>
</head>
<body>
  <article class="card">
    <div class="accent-dot"></div>

    <header class="holder">
      <p class="holder-name">JHON SMITH</p>
      <p class="holder-role">CEO/Founder</p>
    </header>

    <p class="brand">brivolo</p>

    <p class="address">PO BOX 123 your address<br>2nd street london ,USA</p>

    <ul class="contacts">
      <li>
        <svg viewBox="0 0 32 32" aria-hidden="true">
          <rect width="32" height="32" rx="4" fill="#2e8b47"/>
          <path d="M11 7l3 5-2 2c1 3 3 5 6 6l2-2 5 3-2 4c-8 0-16-8-16-16z" fill="#fff"/>
        </svg>
        <span>123 456 7890</span>
      </li>
      <li>
        <svg viewBox="0 0 32 32" aria-hidden="true">
          <rect width="32" height="32" rx="4" fill="#2e8b47"/>
          <rect x="6" y="9" width="20" height="14" fill="none" stroke="#fff" stroke-width="2"/>
          <path d="M6 9l10 8 10-8" fill="none" stroke="#fff" stroke-width="2"/>
        </svg>
        <span>Info@yourcompany.com</span>
      </li>
    </ul>

    <p class="website">www.<span class="site-name">yourcompany</span>.com</p>

    <div class="band">
      <div class="band-green"></div>
      <div class="band-orange"></div>
    </div>
  </article>
</body>
</html>
```